Kem7Dex Letterhead

Need a new letterhead for my law firm.
IDENTIFYING INFORMATION BELOW:
Ansel T Brightwater III
Attorney at Law
Address: 4832 Tillbury Rd, Ste 250, Dallas, TX 75204
Phone: 866-402-7183
Fax: 469-583-0271
Email: kem@kem7dex.example
Website: www.kem7dex.example

Colors
0054AA
0677BA
7BADD7
CADEEF
E8F1F8

Requirements
Must have
• Logo needs to be on the letterhead, along with identifying information which is included in the project description.

```html
<!DOCTYPE html>
<html lang="en">
<head>
<meta charset="utf-8">
<title>Kem7Dex Letterhead</title>
<link rel="stylesheet" href="https://fonts.googleapis.com/css2?family=Open+Sans:wght@400;600;700&display=swap">
<style>
  :root {
    --brand-navy: #0054AA;
    --brand-blue: #0677BA;
    --brand-sky: #7BADD7;
    --ink: #1a1a1a;
    --body-text: #333333;
    --muted: #555555;
    --paper: #ffffff;
    --backdrop: #e9ecef;
  }
  html, body {
    margin: 0;
    padding: 0;
    width: 1200px;
    height: 1142px;
    overflow: hidden;
    background: var(--backdrop);
    font-family: "Open Sans", Arial, sans-serif;
  }
  .letterhead {
    position: absolute;
    left: 224px;
    top: 38px;
    width: 752px;
    height: 1066px;
    background: var(--paper);
    box-shadow: 0 4px 18px rgba(0,0,0,0.12);
    color: var(--body-text);
  }
  .brand {
    position: absolute;
    left: 29px;
    top: 72px;
    display: flex;
    align-items: center;
    gap: 12px;
  }
  .brand-mark {
    width: 26px;
    height: 26px;
    background: var(--brand-navy);
  }
  .brand-name {
    font-size: 40px;
    font-weight: 700;
    color: var(--ink);
    letter-spacing: 1px;
    line-height: 1;
  }
  .attorney {
    position: absolute;
    right: 29px;
    top: 72px;
    text-align: right;
    line-height: 18px;
  }
  .attorney-name {
    font-size: 14px;
    font-weight: 700;
    color: var(--brand-navy);
  }
  .attorney-title {
    font-size: 13px;
    color: var(--muted);
  }
  .meta {
    position: absolute;
    left: 29px;
    top: 220px;
    font-size: 12px;
    line-height: 24px;
    color: var(--muted);
  }
  .date {
    position: absolute;
    right: 29px;
    top: 220px;
    font-size: 13px;
    line-height: 24px;
    color: var(--muted);
  }
  .letter-body {
    position: absolute;
    left: 29px;
    top: 302px;
    width: 694px;
    font-size: 13px;
    line-height: 21px;
  }
  .salutation {
    font-weight: 600;
    font-size: 14px;
    margin: 0 0 12px;
  }
  .letter-body p {
    margin: 0 0 21px;
    text-align: justify;
  }
  .closing {
    position: absolute;
    left: 29px;
    top: 758px;
    font-size: 13px;
    line-height: 21px;
  }
  .closing .signer {
    margin-top: 21px;
    color: var(--ink);
    font-weight: 600;
  }
  .footer-address {
    position: absolute;
    left: 29px;
    top: 960px;
    font-size: 12px;
    line-height: 20px;
    color: var(--muted);
  }
  .footer-rule {
    display: block;
    width: 27px;
    height: 2px;
    background: var(--brand-blue);
    margin-top: 9px;
  }
  .footer-contact {
    position: absolute;
    right: 29px;
    top: 960px;
    display: flex;
    font-size: 12px;
    line-height: 20px;
    color: var(--muted);
  }
  .contact-col {
    padding: 0 10px;
  }
  .contact-col:last-child { padding-right: 0; }
  .contact-col + .contact-col { border-left: 1px solid var(--brand-blue); height: 40px; }
  .contact-row {
    display: flex;
    align-items: center;
    gap: 5px;
  }
  .contact-row svg { width: 9px; height: 9px; fill: var(--brand-navy); }
</style>
</head>
<body>
  <main class="letterhead">
    <header>
      <div class="brand">
        <span class="brand-mark"></span>
        <span class="brand-name">KEM7DEX</span>
      </div>
      <div class="attorney">
        <div class="attorney-name">Ansel T Brightwater III</div>
        <div class="attorney-title">Attorney at Law</div>
      </div>
    </header>

    <div class="meta">
      <div>Re:</div>
      <div>To:</div>
    </div>
    <div class="date">December 29, 2021</div>

    <section class="letter-body">
      <div class="salutation">Dear John,</div>
      <p>Lorem ipsum dolor sit amet, consectetur adipiscing elit. Donec orci purus, luctus vitae dignissim eu, iaculis sed purus. Vivamus faucibus, ipsum nec aliquet viverra, leo mauris condimentum ligula, sit amet sagittis enim ligula quis arcu. Nam egestas tortor id nisi porttitor mattis. In tortor ante, ultricies in suscipit a, tempus non massa. Vivamus et auctor mi. Fusce vel massa nulla. Phasellus nec eros mauris, et scelerisque orci.</p>
      <p>Donec malesuada orci vitae nulla accumsan porta a id massa. Quisque accumsan iaculis magna sit amet fringilla. Maecenas consequat, magna eget tincidunt semper, odio nibh rutrum mi, id feugiat ante nisi eu risus. Vestibulum nunc orci, rhoncus a placerat in, ultricies in mi. Quisque scelerisque sagittis nulla at porttitor. Donec malesuada orci vitae nulla accumsan porta a id massa. Quisque accumsan iaculis magna sit amet fringilla. Maecenas consequat, magna eget tincidunt semper, odio nibh rutrum mi, id feugiat ante nisi eu risus. Vestibulum nunc orci, rhoncus a placerat in, ultricies in mi. Cras mattis varius eros, vel fringilla nisi suscipit eget. Quisque scelerisque sagittis nulla at porttitor.</p>
      <p>Sed id augue vitae urna euismod commodo aliquet a quam. Pellentesque arcu velit, cursus et malesuada ut, consequat et diam. Nullam erat sem, rhoncus id ullamcorper vitae, rhoncus et arcu. In ultricies ultricies nulla, ut rutrum nisi iaculis at. Donec eu magna a metus ornare faucibus. Fusce aliquet faucibus ultricies. Morbi semper, est id tincidunt gravida, sem arcu adipiscing lacus, ac bibendum nulla leo eu purus. Quisque nec diam sed risus consectetur a ccumsan quis quis nibh. Vestibulum id purus lorem.</p>
    </section>

    <div class="closing">
      <div>Sincerily,</div>
      <div class="signer">John Smith</div>
      <div>General Manager</div>
    </div>

    <footer>
      <div class="footer-address">
        <div>4832 Tillbury Rd, Ste 250,</div>
        <div>Dallas, TX 75204</div>
        <span class="footer-rule"></span>
      </div>
      <div class="footer-contact">
        <div class="contact-col">
          <div class="contact-row">
            <svg viewBox="0 0 10 10" aria-hidden="true"><path d="M1 3c0-1 1-2 4-2s4 1 4 2v1H7V3H3v1H1zM2 5h6l1 4H1z"/></svg>
            <span>866-402-7183</span>
          </div>
          <div class="contact-row">
            <svg viewBox="0 0 10 10" aria-hidden="true"><rect x="1" y="4" width="8" height="5" rx="1"/><rect x="2.5" y="1" width="5" height="3"/></svg>
            <span>469-583-0271</span>
          </div>
          <span class="footer-rule"></span>
        </div>
        <div class="contact-col">
          <div class="contact-row">
            <svg viewBox="0 0 10 10" aria-hidden="true"><path d="M1 1l8 4-8 4 2-4z"/></svg>
            <span>kem@kem7dex.example</span>
          </div>
          <div class="contact-row">
            <svg viewBox="0 0 10 10" aria-hidden="true"><circle cx="5" cy="5" r="4"/></svg>
            <span>www.kem7dex.example</span>
          </div>
        </div>
      </div>
    </footer>
  </main>
</body>
</html>
```